Unspooling Ledgers - Podcast Cover

Unspooling Ledgers is a weekly podcast that dispels some of the myths about conventional economic thinking and provides a new way of thinking about issues that are faced by the global economy. It's insightful, thought-provoking and, most importantly, fun. We are refreshing the look and sound of the podcast. I have attached a copy of the old amateur design (which I did!)

Target Market(s)

Male oriented, smart folk with an interest in politics and economics

Font styles to use
Sans Serif

Requirements
Must have
• Clearly visible title, even when reduced in size. Must be 3000 pixels by 3000 pixels.
Nice to have
• This podcast challenges the status quo. It should reflect that. Photos and names of the hosts. Actually, because th ephotos are so different, we'd be open to the idea of a caricature if you can do that within the price.

```html
<!DOCTYPE html>
<html lang="en">
<head>
<meta charset="utf-8">
<title>Unspooling Ledgers Podcast Cover</title>
<link href="https://fonts.googleapis.com/css2?family=Archivo+Black&family=Kalam:wght@700&display=swap" rel="stylesheet">
<style>
  :root {
    --paper: #f2f2f2;
    --ink: #0a0a0a;
    --red: #c4262e;
    --white: #ffffff;
    --cash-light: #e4e3cc;
    --cash-dark: #8f9279;
    --gold: #c79a3a;
  }
  html, body { margin: 0; padding: 0; overflow: hidden; background: var(--paper); }
  .cover {
    position: relative;
    width: 1200px;
    height: 1200px;
    background: var(--paper);
    overflow: hidden;
    font-family: "Archivo Black", "Arial Black", sans-serif;
  }
  .cover svg { position: absolute; inset: 0; }
  .title-red { fill: var(--red); }
  .title-solid { fill: var(--ink); }
  .title-outline { fill: var(--white); stroke: var(--ink); stroke-width: 3; paint-order: stroke; }
  .rule { stroke: #333; stroke-width: 2.5; stroke-linecap: round; }
  .host-name { font-size: 44px; }
  .host-name .first { fill: var(--ink); }
  .host-name .last { fill: var(--red); }
  .host-title { font-family: "Kalam", cursive; font-size: 30px; fill: var(--red); }
</style>
</head>
<body>
<div class="cover">
  <svg viewBox="0 0 1200 1200" width="1200" height="1200">
    <defs>
      <linearGradient id="cashTone" x1="0" y1="0" x2="1" y2="1">
        <stop offset="0" stop-color="var(--cash-light)"/>
        <stop offset="1" stop-color="var(--cash-dark)"/>
      </linearGradient>
      <linearGradient id="hostOneTone" x1="0" y1="0" x2="0" y2="1">
        <stop offset="0" stop-color="#e3e3e6"/>
        <stop offset="1" stop-color="#2a8fa6"/>
      </linearGradient>
      <linearGradient id="hostTwoTone" x1="0" y1="0" x2="0" y2="1">
        <stop offset="0" stop-color="#3a3636"/>
        <stop offset="1" stop-color="#d8d6d0"/>
      </linearGradient>
      <radialGradient id="coinTone" cx="0.4" cy="0.35" r="0.7">
        <stop offset="0" stop-color="#f0d27a"/>
        <stop offset="1" stop-color="var(--gold)"/>
      </radialGradient>
    </defs>

    <!-- double frame -->
    <g class="frame" fill="none" stroke="var(--ink)">
      <rect x="38" y="38" width="1124" height="1124" rx="52" stroke-width="3"/>
      <rect x="48" y="48" width="1104" height="1104" rx="44" stroke-width="1.5"/>
    </g>

    <!-- fanned banknotes -->
    <path class="cash-fan" role="img" aria-label="Fanned stack of hundred-dollar banknotes"
          d="M226 40 L300 0 L972 0 L960 40 L905 120 L800 220 L640 280 L530 295 L470 255 L380 205 L300 150 L240 95 Z"
          fill="url(#cashTone)"/>

    <!-- title -->
    <line class="rule" x1="90" y1="397" x2="469" y2="397"/>
    <line class="rule" x1="736" y1="397" x2="1116" y2="397"/>
    <text class="title-red" x="600" y="422" font-size="84" text-anchor="middle">THE</text>

    <text class="title-solid" x="600" y="559" font-size="146" text-anchor="middle"
          textLength="1022" lengthAdjust="spacingAndGlyphs">UNSPOOLING</text>

    <text class="title-outline" x="600" y="702" font-size="154" text-anchor="middle"
          textLength="1000" lengthAdjust="spacing">LEDGERS</text>

    <line class="rule" x1="90" y1="779" x2="357" y2="779"/>
    <line class="rule" x1="850" y1="779" x2="1116" y2="779"/>
    <text class="title-red" x="603" y="807" font-size="86" text-anchor="middle">PODCAST</text>

    <!-- host one -->
    <circle cx="273" cy="956" r="115" fill="var(--white)"/>
    <circle cx="273" cy="956" r="104" fill="url(#hostOneTone)" role="img" aria-label="Portrait photo of host Neil Hollis"/>
    <circle cx="354" cy="1043" r="34" fill="url(#coinTone)" role="img" aria-label="Gold dollar coin"/>
    <text class="host-name" x="410" y="950"><tspan class="first">NEIL</tspan></text>
    <text class="host-name" x="410" y="988"><tspan class="last">HOLLIS</tspan></text>

    <!-- host two -->
    <circle cx="767" cy="956" r="115" fill="var(--white)"/>
    <circle cx="767" cy="956" r="104" fill="url(#hostTwoTone)" role="img" aria-label="Portrait photo of host Prof Clive Brant"/>
    <circle cx="848" cy="1043" r="34" fill="url(#coinTone)" role="img" aria-label="Gold dollar coin"/>
    <text class="host-title" x="903" y="912">Prof</text>
    <text class="host-name" x="905" y="953"><tspan class="first">CLIVE</tspan></text>
    <text class="host-name" x="905" y="994"><tspan class="last">BRANT</tspan></text>
  </svg>
</div>
</body>
</html>
```